Website Design Project for Beauty & Wellness Professionals

As background information, I have a website that is focused on Beauty & Wellness Professionals:
- Job Search (www.trilhavelora.com)
- Business Classifieds (negocios.trilhavelora.com)
- Freelancer Classifieds (freelancer.trilhavelora.com)
- Course Reviews (cursos.trilhavelora.com)

All those websites use standard templates.

I need a DESIGN for the HOME PAGE (no coding) of the Website Platform that consolidates the four platforms under the same design.

Website designs that we like:
- quovenda.com
- mirtelpeek.com

Target Market(s)

Brazilian Professionals from Beauty & Wellness sector

Industry/Entity Type

Business

Requirements
Must have
• Website designs that we like:
- quovenda.com
- mirtelpeek.com

```html
<!DOCTYPE html>
<html lang="en">
<head>
<meta charset="utf-8">
<title>Trilha Velora – Home</title>
<link rel="stylesheet" href="https://fonts.googleapis.com/css2?family=Oswald:wght@300;400;600;700&family=Open+Sans:wght@400;600;700&display=swap">
<style>
:root{
  --teal:#35a7c8;
  --blue:#3aa6cc;
  --green:#4caa2a;
  --green-dark:#2f8a1c;
  --orange:#e0642a;
  --yellow:#f7bf2b;
  --yellow-dark:#e8a514;
  --ink:#333;
  --muted:#666;
  --line:#dcdcdc;
  --footer:#efefef;
}
*{box-sizing:border-box;margin:0;padding:0}
html,body{width:1200px;height:2410px;overflow:hidden;background:#fff}
body{position:relative;font-family:"Open Sans",Arial,sans-serif;color:var(--ink)}
.abs{position:absolute}

/* header */
.site-header{position:absolute;left:0;top:0;width:1200px;height:84px;background:linear-gradient(#fff,#f1f1f1);border-bottom:1px solid #e2e2e2}
.brand{position:absolute;left:24px;top:20px;display:flex;align-items:center;gap:10px;font-size:27px;color:var(--teal);font-weight:400}
.brand-dot{width:40px;height:40px;border-radius:50%;background:var(--teal)}
.main-nav{position:absolute;left:286px;top:27px;display:flex;gap:12px}
.main-nav a{display:block;height:29px;line-height:29px;padding:0 16px;border-radius:8px;background:var(--teal);color:#fff;font-size:16px;text-decoration:none}
.account-links{position:absolute;left:830px;top:34px;display:flex;gap:22px;font-size:14px;font-weight:700;color:#2aa37a}
.btn-advertise{position:absolute;left:993px;top:22px;width:187px;height:42px;border-radius:8px;background:linear-gradient(#fcd34a,var(--yellow-dark));color:#a8480e;font-size:19px;text-align:center;line-height:42px;border:1px solid #d99a10}

/* hero */
.hero{position:absolute;left:0;top:84px;width:1200px;height:507px;background:radial-gradient(ellipse at 45% 70%,#d79a3e 0%,#b8893f 25%,#8fb35a 55%,#a6c770 75%,#7fa048 100%)}
.hero-title{position:absolute;left:0;top:60px;width:1200px;text-align:center;font-family:"Oswald",sans-serif;font-weight:700;font-size:60px;line-height:72px;color:#fff;letter-spacing:-.5px;
  text-shadow:0 0 2px var(--green-dark),2px 2px 0 var(--green-dark),-2px -2px 0 var(--green-dark),2px -2px 0 var(--green-dark),-2px 2px 0 var(--green-dark),0 4px 6px rgba(0,0,0,.35)}
.search-bar{position:absolute;left:100px;top:269px;width:1000px;height:73px;border-radius:10px;background:rgba(40,40,40,.85)}
.field{position:absolute;top:15px;height:43px;border-radius:6px;background:#fff;font-size:19px;color:#666;line-height:43px;padding-left:16px}
.field-select{left:12px;width:174px}
.field-select svg{position:absolute;right:12px;top:17px}
.field-location{left:197px;width:209px}
.field-keyword{left:417px;width:392px}
.btn-search{position:absolute;left:823px;top:15px;width:163px;height:43px;border-radius:6px;background:linear-gradient(#fcd34a,var(--yellow-dark));color:#6b3b08;font-size:19px;text-align:center;line-height:43px}

/* jobs grid */
.section-title{position:absolute;left:16px;top:604px;font-family:"Oswald",sans-serif;font-weight:600;font-size:46px;color:var(--blue);letter-spacing:-.5px}
.section-sub{position:absolute;left:16px;top:660px;font-family:"Oswald",sans-serif;font-weight:300;font-size:29px;color:#444}
.job-tile{position:absolute;width:244px;height:177px}
.job-tile .photo{position:absolute;inset:0}
.job-tile .label{position:absolute;left:0;top:130px;height:34px;line-height:34px;padding:0 12px;color:#fff;font-size:20px}
.label-green{background:var(--green)}
.label-blue{background:var(--blue)}
.label-orange{background:var(--orange)}

/* sidebar */
.promo{position:absolute;left:821px;top:605px;width:366px;height:169px;background:repeating-conic-gradient(from 0deg at 50% 100%,#7dc760 0 8deg,#8fd472 8deg 16deg)}
.promo-text{position:absolute;left:0;top:14px;width:366px;text-align:center;font-family:"Oswald",sans-serif;font-weight:600;font-size:24px;line-height:28px;color:#fff;text-shadow:0 1px 2px rgba(0,0,0,.35)}
.promo-btn{position:absolute;left:66px;top:97px;width:234px;height:56px;border-radius:10px;background:linear-gradient(#f6923c,#e0591c);color:#fff;font-size:21px;text-align:center;line-height:56px;border:2px solid #c94d14}
.ad{position:absolute;left:821px;top:789px;width:366px;height:305px;background:#a62a2a}
.ad-brand{position:absolute;left:0;top:12px;width:366px;display:flex;justify-content:center;align-items:center;gap:10px;color:#fff;font-size:25px}
.ad-brand i{width:26px;height:26px;border-radius:50%;background:#fff;display:block}
.ad-copy{position:absolute;left:0;top:66px;width:366px;text-align:center;color:#fff;font-weight:700;font-size:21px;line-height:27px}
.ad-shirt{position:absolute;left:83px;top:124px;width:200px;height:166px;background:linear-gradient(#2a2a2a,#1a1a1a);border-radius:22px 22px 6px 6px}
.ad-cta{position:absolute;left:109px;top:254px;width:148px;height:36px;background:#1a8b92;color:#fff;font-weight:700;font-size:17px;text-align:center;line-height:36px}
.ad-badge{position:absolute;right:4px;top:4px;width:14px;height:14px;background:#c8e3f0}
.side-heading{position:absolute;left:821px;font-weight:700;font-size:19px;color:#222;width:366px;border-bottom:1px solid var(--line);padding-bottom:4px}
.connect-line{position:absolute;left:821px;top:1179px;width:366px;font-size:14px;line-height:20px;color:#333}
.connect-line a{color:#1f67b0;text-decoration:none}
.connect-line .sq{display:inline-block;width:13px;height:13px;background:#3b5998;vertical-align:-1px;margin-right:5px}
.friends{position:absolute;left:821px;top:1224px;display:flex;gap:4px}
.friends div{width:61px;height:61px}
.uncover{position:absolute;left:821px;top:1289px;font-size:14px;font-weight:700;color:#1f67b0}
.vacancies{position:absolute;left:821px;top:1381px;width:366px;list-style:none}
.vacancies li{height:33px;line-height:32px;border-bottom:1px solid #e8e8e8;font-size:15px;color:#444;padding-left:2px}
.vacancies li::before{content:"›";color:#888;margin-right:3px}

/* footer */
.site-footer{position:absolute;left:0;top:2133px;width:1200px;height:277px;background:var(--footer);border-top:1px solid #e0e0e0}
.foot-col{position:absolute;top:40px}
.foot-col h3{font-size:20px;font-weight:700;color:#333;margin-bottom:8px}
.foot-col ul{list-style:none}
.foot-col li{font-size:14px;line-height:17.6px;color:#333}
.foot-input{position:absolute;height:42px;border-radius:6px;background:#e4e4e4;border:1px solid #d0d0d0;font-size:13px;color:#555;line-height:40px;padding-left:14px}
.foot-btn{position:absolute;left:679px;top:2308px;width:126px;height:40px;border-radius:6px;background:#8a8a8a;color:#fff;font-size:15px;text-align:center;line-height:40px}
.social{position:absolute;left:925px;top:2207px;display:flex;gap:9px}
.social i{width:35px;height:35px;border-radius:50%;background:#8c8c8c;display:block}
.newsletter-text{position:absolute;left:925px;top:2258px;width:240px;font-size:12.5px;line-height:16px;color:#333}
.newsletter-input{position:absolute;left:923px;top:2302px;width:225px;height:32px;border-radius:16px;background:#8a8a8a;color:#eee;font-size:13px;line-height:32px;padding-left:18px}
.newsletter-submit{position:absolute;left:928px;top:2350px;font-size:13px;font-weight:700;color:#333}
</style>
</head>
<body>

<header class="site-header">
  <div class="brand"><span class="brand-dot"></span>Trilha Velora</div>
  <nav class="main-nav">
    <a>Home</a><a>Professionals</a><a>Business</a><a>Partners</a><a>Blog</a>
  </nav>
  <div class="account-links"><span>SIGN UP</span><span>LOG IN</span></div>
  <div class="btn-advertise">Advertise Now!</div>
</header>

<section class="hero" role="img" aria-label="Photo of a beauty salon interior with orange salon chairs">
  <h1 class="hero-title">Espaco para Empresas e Profissionais de<br>Beleza, Estetita e Bem-estar</h1>
  <form class="search-bar">
    <div class="field field-select">Hairdresser
      <svg width="14" height="9" viewBox="0 0 14 9"><path d="M0 0h14L7 9z" fill="#555"/></svg>
    </div>
    <div class="field field-location">Location</div>
    <div class="field field-keyword">Job Title, Keyworkds or Company</div>
    <div class="btn-search">Search</div>
  </form>
</section>

<h2 class="section-title">Find the best jobs that fits for you!</h2>
<p class="section-sub">See our list of categorized jobs below.</p>

<!-- row 1 -->
<div class="job-tile" style="left:8px;top:728px"><div class="photo" role="img" aria-label="Photo of two hairdressers in a salon" style="background:linear-gradient(135deg,#c9b49a,#5a4a3c)"></div><span class="label label-green">Hairdresser</span></div>
<div class="job-tile" style="left:278px;top:728px"><div class="photo" role="img" aria-label="Photo of colourful cleaning products" style="background:linear-gradient(135deg,#3fa0e0,#f0d040 60%,#e04a6a)"></div><span class="label label-blue">Cleaning</span></div>
<div class="job-tile" style="left:546px;top:728px"><div class="photo" role="img" aria-label="Photo of an eyebrow being shaped" style="background:linear-gradient(135deg,#e9d3c3,#8a6a58)"></div><span class="label label-orange">Eyebrow Designer</span></div>
<!-- row 2 -->
<div class="job-tile" style="left:8px;top:952px"><div class="photo" role="img" aria-label="Photo of a nurse caring for an elderly woman" style="background:linear-gradient(135deg,#d8c8b8,#9aa3c2)"></div><span class="label label-green">Nurse</span></div>
<div class="job-tile" style="left:278px;top:952px"><div class="photo" role="img" aria-label="Photo of a facial spa treatment with a flower" style="background:linear-gradient(135deg,#e8c4a8,#f4eee6)"></div><span class="label label-blue">Esthetician</span></div>
<div class="job-tile" style="left:546px;top:952px"><div class="photo" role="img" aria-label="Photo of a physiotherapist treating a foot" style="background:linear-gradient(135deg,#e4dccf,#8a7a66)"></div><span class="label label-orange">Physiotherapist</span></div>
<!-- row 3 -->
<div class="job-tile" style="left:8px;top:1179px"><div class="photo" role="img" aria-label="Photo of nails being painted pink" style="background:linear-gradient(135deg,#d64a7a,#f2c3b0)"></div><span class="label label-green">Manicure / Pedicure</span></div>
<div class="job-tile" style="left:278px;top:1179px"><div class="photo" role="img" aria-label="Photo of makeup being applied" style="background:linear-gradient(135deg,#5a3a2a,#e4b898)"></div><span class="label label-blue">Makeup Artist</span></div>
<div class="job-tile" style="left:546px;top:1179px"><div class="photo" role="img" aria-label="Photo of a practitioner in blue scrubs with a patient" style="background:linear-gradient(135deg,#2a6aa8,#d8dde2)"></div><span class="label label-orange">Practitioner</span></div>
<!-- row 4 -->
<div class="job-tile" style="left:8px;top:1400px"><div class="photo" role="img" aria-label="Photo of two hairdressers in a salon" style="background:linear-gradient(135deg,#c9b49a,#5a4a3c)"></div><span class="label label-green">Hairdresser</span></div>
<div class="job-tile" style="left:278px;top:1400px"><div class="photo" role="img" aria-label="Photo of colourful cleaning products" style="background:linear-gradient(135deg,#3fa0e0,#f0d040 60%,#e04a6a)"></div><span class="label label-blue">Cleaning</span></div>
<div class="job-tile" style="left:546px;top:1400px"><div class="photo" role="img" aria-label="Photo of an eyebrow being shaped" style="background:linear-gradient(135deg,#e9d3c3,#8a6a58)"></div><span class="label label-orange">Eyebrow Designer</span></div>
<!-- row 5 -->
<div class="job-tile" style="left:8px;top:1625px"><div class="photo" role="img" aria-label="Photo of a nurse caring for an elderly woman" style="background:linear-gradient(135deg,#d8c8b8,#9aa3c2)"></div><span class="label label-green">Nurse</span></div>
<div class="job-tile" style="left:278px;top:1625px"><div class="photo" role="img" aria-label="Photo of a facial spa treatment with a flower" style="background:linear-gradient(135deg,#e8c4a8,#f4eee6)"></div><span class="label label-blue">Esthetician</span></div>
<div class="job-tile" style="left:546px;top:1625px"><div class="photo" role="img" aria-label="Photo of a physiotherapist treating a foot" style="background:linear-gradient(135deg,#e4dccf,#8a7a66)"></div><span class="label label-orange">Physiotherapist</span></div>

<aside>
  <div class="promo">
    <p class="promo-text">Owners Salons, Spas and Clinics<br>Advertise Your Job Vacancy (FREE)!</p>
    <div class="promo-btn">Advertise Now!</div>
  </div>

  <div class="ad">
    <span class="ad-badge"></span>
    <div class="ad-brand"><i></i>Norvane.</div>
    <p class="ad-copy">Norvane &amp; Codelane teamed<br>up to offer this custom shirt!</p>
    <div class="ad-shirt" role="img" aria-label="Photo of a black printed t-shirt"></div>
    <div class="ad-cta">Get it now</div>
  </div>

  <h3 class="side-heading" style="top:1132px">Inside Connections</h3>
  <p class="connect-line"><span class="sq"></span><a>Marisa Quelhas</a>, <a>Tainá Orvalho</a> and 24 other friends use <a>Mirtelpeek</a>.</p>
  <div class="friends">
    <div role="img" aria-label="Friend profile photo" style="background:#9a8a7a"></div>
    <div role="img" aria-label="Friend profile photo" style="background:#5a4a3a"></div>
    <div role="img" aria-label="Friend profile photo" style="background:#6a7ab0"></div>
    <div role="img" aria-label="Friend profile photo" style="background:#8a9ab8"></div>
    <div role="img" aria-label="Friend profile photo" style="background:#c8c0b8"></div>
  </div>
  <p class="uncover">Uncover Inside Connections</p>

  <h3 class="side-heading" style="top:1334px">Job Vacancies</h3>
  <ul class="vacancies">
    <li>Assistant Hairdresser (39)</li>
    <li>Assistant Cleaning (5)</li>
    <li>Hairdresser (125)</li>
    <li>Epilator (28)</li>
    <li>Designer Eyebrow (11)</li>
    <li>Featured (24)</li>
    <li>Nurse (2)</li>
    <li>Esthetician (60)</li>
    <li>Physiotherapist (9)</li>
    <li>Management / Coordination (17)</li>
    <li>Manicure and Pedicure (256)</li>
    <li>Makeup artist (8)</li>
    <li>Practitioner (22)</li>
    <li>Other (15)</li>
    <li>Podiatrist (13)</li>
    <li>Reception / Customer Service (35)</li>
    <li>Sales Cosmetics (22)</li>
  </ul>
</aside>

<footer class="site-footer">
  <div class="foot-col" style="left:22px">
    <h3>Main Navigation</h3>
    <ul><li>Home</li><li>About Us</li><li>Professionals</li><li>Business</li><li>Partners</li><li>Blog</li><li>Contact Us</li></ul>
  </div>
  <div class="foot-col" style="left:299px">
    <h3>Job Categories</h3>
    <ul><li>Hairdresser</li><li>Beautician</li><li>Manicure</li><li>Massage therapist</li><li>Epilator</li><li>Reception</li><li>Sales</li></ul>
  </div>
  <div class="foot-col" style="left:543px"><h3>Search for your job!</h3></div>
  <div class="foot-col" style="left:928px"><h3>Connect With Us</h3></div>
</footer>
<div class="foot-input" style="left:538px;top:2208px;width:267px">Digite aqui a vaga que voce procura!</div>
<div class="foot-input" style="left:538px;top:2258px;width:267px">Localizacao</div>
<div class="foot-input" style="left:538px;top:2308px;width:132px;height:40px;line-height:38px">1 km
  <svg style="position:absolute;right:12px;top:15px" width="11" height="8" viewBox="0 0 11 8"><path d="M0 0h11L5.5 8z" fill="#555"/></svg>
</div>
<div class="foot-btn">search</div>
<div class="social"><i></i><i></i><i></i><i></i><i></i></div>
<p class="newsletter-text">subscribe to our monthly newsletter and get the best deals and discounts</p>
<div class="newsletter-input">enter email address</div>
<p class="newsletter-submit">subscribe now <svg width="10" height="10" viewBox="0 0 10 10"><path d="M2 1l6 4-6 4z" fill="#333"/></svg></p>

</body>
</html>
```